Corporate travel agency website design

Hello I need a website design that will look professional. I want that anyone that gos on our site understands that we are a large successful company. I want it to be up to par with other large companies. The site should be sleek and neat.
Below I will attach my logo. A recent one page add I made and content for my add that will be used for the website.

```html
<!DOCTYPE html>
<html lang="en">
<head>
<meta charset="utf-8">
<title>Meridian Travel — Business Travel Reinvented</title>
<link href="https://fonts.googleapis.com/css2?family=Poppins:wght@300;400;500;600;700;800&display=swap" rel="stylesheet">
<style>
:root{
  --navy:#081838;
  --navy-line:#1e2f55;
  --ink:#0b1a3b;
  --text:#3b4150;
  --white:#ffffff;
  --sky:#d4effa;
  --accent:#bfe8f7;
}
*{margin:0;padding:0;box-sizing:border-box}
html,body{width:1200px;height:3367px;overflow:hidden}
body{position:relative;font-family:'Poppins',sans-serif;background:var(--white);color:var(--text)}
.abs{position:absolute}

/* header */
.site-header{left:0;top:0;width:1200px;height:100px;background:var(--navy)}
.brand-mark{left:161px;top:22px;width:28px;height:28px;border:1.5px solid var(--white);border-radius:50%}
.brand{left:105px;top:60px;width:140px;text-align:center;color:var(--white);font-size:10px;font-weight:400;letter-spacing:1px;white-space:nowrap}
.nav a{position:absolute;top:44px;font-size:10.5px;color:#c9d0de;text-decoration:none;letter-spacing:.3px}
.nav a.active{color:var(--white);font-weight:600}
.nav .sep{position:absolute;top:42px;width:1px;height:14px;background:#35456a}
.nav .cta{top:31px;left:967px;width:122px;height:38px;border:1px solid #7f8bab;color:var(--white);font-weight:600;line-height:36px;text-align:center}

/* hero */
.hero{left:0;top:100px;width:1200px;height:535px;background:linear-gradient(90deg,#f4f6f8 0%,#eef2f5 35%,#c9ced4 62%,#4a4d55 85%,#2a2c33 100%)}
.hero-title{left:112px;top:248px;font-size:44px;line-height:48px;font-weight:800;color:var(--ink);letter-spacing:.3px}
.hero-sub{left:112px;top:352px;font-size:12.5px;line-height:17px;letter-spacing:1.6px;color:var(--ink)}
.btn-talk{left:111px;top:414px;width:155px;height:46px;background:var(--navy);color:var(--white);font-size:12px;font-weight:600;display:flex;align-items:center;justify-content:center;gap:8px}

/* why */
.why-band{left:0;top:635px;width:1200px;height:454px;background:var(--navy)}
.why-photo{left:110px;top:693px;width:462px;height:458px;background:linear-gradient(180deg,#bcd9f0 0%,#e8f2f9 45%,#f2f7fb 70%,#cfe3f1 100%)}
.why-title{left:635px;top:700px;font-size:28px;font-weight:600;color:var(--white);white-space:nowrap}
.why-sub{left:638px;top:748px;padding-left:18px;border-left:3px solid var(--white);font-size:12.5px;line-height:18px;letter-spacing:1.5px;color:var(--white);width:450px}
.why-body{left:636px;top:805px;width:450px;font-size:10.4px;line-height:19.2px;color:#dfe4ee}
.why-body p+p{margin-top:14px}

/* services */
.section-title{left:0;top:1210px;width:1200px;text-align:center;font-size:28px;font-weight:500;color:var(--ink);letter-spacing:.3px}
.title-bar{left:584px;top:1257px;width:32px;height:4px;background:var(--accent)}
.svc-photo{background:linear-gradient(160deg,#d9dfe3,#9aa3a8 55%,#4b525a)}
.svc-icon{width:58px;height:58px;border:2px solid var(--ink);border-radius:50%;display:flex;align-items:center;justify-content:center}
.svc-icon span{width:44px;height:44px;border-radius:50%;background:var(--accent);display:flex;align-items:center;justify-content:center}
.svc-title{font-size:18px;color:var(--ink);font-weight:400;white-space:nowrap}
.svc-title b{font-weight:700}
.svc-body{font-size:10.2px;line-height:19.2px;color:var(--text)}
.btn-more{height:40px;border:1px solid #9aa0ab;font-size:9.5px;font-weight:700;color:var(--ink);display:flex;align-items:center;justify-content:center}
.connector{height:1.5px;background:var(--ink)}

/* features */
.feature-band{left:0;top:2751px;width:1200px;height:276px;background:var(--sky)}
.feature{top:2823px;width:186px;height:135px;background:var(--white);text-align:center}
.feature svg{position:absolute;left:73px;top:24px}
.feature p{position:absolute;left:0;top:87px;width:100%;font-size:11.3px;line-height:13px;font-weight:600;color:var(--ink)}

/* footer */
.site-footer{left:0;top:3027px;width:1200px;height:340px;background:var(--navy);color:#d8deea}
.foot-circle{left:322px;top:3112px;width:44px;height:44px;border:1.5px solid var(--white);border-radius:50%}
.foot-brand{left:214px;top:3192px;width:260px;text-align:center;color:var(--white);font-size:18px;font-weight:400;letter-spacing:2px;white-space:nowrap}
.social{top:3234px;width:26px;height:26px;border:1px solid var(--navy-line)}
.social.on{background:var(--accent)}
.vline{width:1px;height:177px;top:3117px;background:var(--navy-line)}
.foot-h{font-size:12.5px;font-weight:600;color:var(--white);letter-spacing:.5px}
.foot-u{height:1px;background:#4b5a7d}
.foot-item{font-size:10.5px;line-height:14px;color:#d8deea;display:flex;gap:8px;align-items:flex-start}
.foot-link{left:836px;font-size:10.5px;color:#d8deea}
.copy-line{left:210px;top:3307px;width:780px;height:1px;background:var(--navy-line)}
.copy{left:0;top:3330px;width:1200px;text-align:center;font-size:10px;color:#c3cad9}
</style>
</head>
<body>

<header class="abs site-header">
  <div class="abs brand-mark"></div>
  <div class="abs brand">MERIDIAN TRAVEL</div>
  <nav class="nav">
    <a class="active" style="left:518px">HOME</a>
    <span class="sep" style="left:582px"></span>
    <a style="left:613px">ABOUT US</a>
    <span class="sep" style="left:697px"></span>
    <a style="left:727px">WHY CHOOSE US</a>
    <span class="sep" style="left:846px"></span>
    <a style="left:876px">RESOURCES</a>
    <a class="cta">CONTACT US</a>
  </nav>
</header>

<section class="abs hero" role="img" aria-label="Business travellers seated in an airport lounge using phone and laptop"></section>
<h1 class="abs hero-title">BUSINESS<br>TRAVEL REINVENTED</h1>
<p class="abs hero-sub">MERIDIAN TRAVEL IS A GLOBAL LEADER IN BUSINESS TRAVEL<br>MANAGEMENT SERVICES.</p>
<a class="abs btn-talk">
  <svg width="20" height="18" viewBox="0 0 20 18" fill="none" stroke="#fff" stroke-width="1.6"><path d="M3 11V9a7 7 0 0 1 14 0v2"/><rect x="1.5" y="10" width="3.5" height="5" rx="1"/><rect x="15" y="10" width="3.5" height="5" rx="1"/><path d="M17 15c0 2-3 2.5-6 2.5"/></svg>
  TALK TO US
</a>

<section class="abs why-band"></section>
<div class="abs why-photo" role="img" aria-label="Two business people shaking hands beside an airliner at an airport window"></div>
<h2 class="abs why-title">WHY CHOOSE MERIDIAN TRAVEL?</h2>
<p class="abs why-sub">MERIDIAN TRAVEL IS A GLOBAL LEADER IN BUSINESS TRAVEL MANAGEMENT SERVICES.</p>
<div class="abs why-body">
  <p>Meridian Travel is a global leader in business travel management services. We drive savings, efficiency, and unparalleled service to businesses and their travelers all around the world.</p>
  <p>If you are looking for a tailored travel managed solution focused on offering white glove service and fulfilling your individual preferences ,while delivering customer excellence, you've come to the right place. At Meridian Travel, our mission is to have you focus on your day to day business while we handle all of the logistics and details for the most successful all encompassing travel experience. From emergency passport arrangements to last minute cancellations, re-bookings, and other intricate travel challenges, Meridian Travel is well versed in handling the routine array of travel services, as well as solving any travel related issue that might arise.</p>
</div>

<h2 class="abs section-title">TRAVEL MANAGEMENT SERVICE</h2>
<div class="abs title-bar"></div>

<!-- service 1 -->
<div class="abs svc-icon" style="left:209px;top:1376px"><span><svg width="26" height="26" viewBox="0 0 26 26" fill="none" stroke="#0b1a3b" stroke-width="1.6"><circle cx="15" cy="7" r="5"/><path d="M15 4.5v5M3 16h5l5 2h6l4-3M3 22h6l5 1 9-5"/></svg></span></div>
<h3 class="abs svc-title" style="left:211px;top:1446px">UNPARALLED <b>SERVICE</b></h3>
<p class="abs svc-body" style="left:211px;top:1486px;width:362px">Meridian Travel Is Famous For Our Concierge Style Approach To Travel. From Detailed Planning, To Commercial Or Private Air Travel, Transportation, Including Car Rentals, Chauffers, Busses For Larger Groups, Hotels, All Styles Of Lodging Accomodations, Special Event Planning And More, Meridian Travel Is Like Having Your Own Personal Or Corporate Travel Butler.</p>
<a class="abs btn-more" style="left:211px;top:1631px;width:121px">LEARN MORE</a>
<div class="abs connector" style="left:576px;top:1424px;width:164px"></div>
<div class="abs svc-photo" style="left:702px;top:1307px;width:386px;height:433px" role="img" aria-label="Business travellers with luggage walking through an airport terminal"></div>

<!-- service 2 -->
<div class="abs svc-photo" style="left:110px;top:1780px;width:387px;height:433px;background:linear-gradient(120deg,#2b2f36,#8b8478 45%,#e6d3b4 75%,#f3efe8)" role="img" aria-label="Three colleagues reviewing a travel brochure together"></div>
<div class="abs connector" style="left:408px;top:1836px;width:157px"></div>
<div class="abs svc-icon" style="left:585px;top:1801px"><span><svg width="24" height="26" viewBox="0 0 24 26" fill="none" stroke="#0b1a3b" stroke-width="1.6"><rect x="3" y="4" width="13" height="18"/><path d="M6 9h7M6 13h7M6 17h4"/><rect x="12" y="12" width="9" height="12" fill="#bfe8f7"/><path d="M14 15h5M14 18h1M17 18h1M14 21h1M17 21h1"/></svg></span></div>
<h3 class="abs svc-title" style="left:588px;top:1872px">BUDGET &amp; TRAVEL <b>SPEND REPORTING</b></h3>
<p class="abs svc-body" style="left:588px;top:1911px;width:400px">Having a travel management service will ensure that your company enforces corporate compliance and maintains control over travel decisions. This ensures that your employees stick to your budget, which in turn will protect your bottom line. Travel expenses can be costly. Having a savvy and experienced corporate travel manager who can access deep discounts not available to the public will ensure your travel is booked across the board at the lowest prices expenses are kept under control. Travel reporting is critical to optimizing budgets, streamlining expense reports, and recognizing key trends. Meridian Travel customizes travel spend reports, by team, project, department etc, so companies can accurately track travel expenses, and make critical decisions based on the spend.</p>
<a class="abs btn-more" style="left:591px;top:2153px;width:122px">LEARN MORE</a>

<!-- service 3 -->
<div class="abs svc-icon" style="left:209px;top:2295px"><span><svg width="26" height="26" viewBox="0 0 26 26" fill="none" stroke="#0b1a3b" stroke-width="1.6"><circle cx="13" cy="13" r="9"/><path d="M13 8v5l3 3M4 6l2 2M22 6l-2 2"/></svg></span></div>
<h3 class="abs svc-title" style="left:211px;top:2366px">EFFICI<b>ENCY</b></h3>
<p class="abs svc-body" style="left:211px;top:2405px;width:386px">Time is your most valuable tool! Our goal at Meridian Travel is to have your employees' complete focus be on your core business, while having us handle all the logistics for their travel. One of the most appreciated services we offer is the management of travel headaches. Unforeseen circumstances such as cancellations, missed flights, cancelled flights, last minute bookings or changed plans, can take hours to rectify. Meridian Travel handles all of these tedious repositionings expeditiously, saving your employees precious time. Give your company a competitive edge by having Meridian Travel handle your team's travel arrangements.</p>
<a class="abs btn-more" style="left:211px;top:2597px;width:121px">LEARN MORE</a>
<div class="abs connector" style="left:612px;top:2316px;width:150px"></div>
<div class="abs svc-photo" style="left:703px;top:2249px;width:386px;height:433px;background:linear-gradient(170deg,#eef0f0,#c9cccf 50%,#253356 80%,#e7e4df)" role="img" aria-label="Business travellers pulling rolling suitcases through an airport"></div>

<!-- features -->
<section class="abs feature-band"></section>
<div class="abs feature" style="left:110px"><svg width="40" height="40" viewBox="0 0 40 40" fill="none" stroke="#0b1a3b" stroke-width="1.5"><path d="M8 34V18l4-6 2 2-2 6 6-8 2 2-4 8M22 34V20l3-8 2 1-1 7 4-6 2 1-3 7 3-4 2 1-4 9v7"/><path d="M16 6l1-3M20 7l2-3M12 8l-2-2"/></svg><p>WHITH<br>GLOVE SERVICE</p></div>
<div class="abs feature" style="left:309px"><svg width="40" height="40" viewBox="0 0 40 40" fill="none" stroke="#0b1a3b" stroke-width="1.5"><rect x="9" y="12" width="18" height="22"/><path d="M13 18h10M13 22h10M13 26h6"/><circle cx="29" cy="10" r="6"/><path d="M26.5 10l2 2 3-4"/><path d="M5 28h8v6H5z"/></svg><p>CORPORATE TRAVEL<br>POLICY COMPLIANCE</p></div>
<div class="abs feature" style="left:507px"><svg width="40" height="40" viewBox="0 0 40 40" fill="none" stroke="#0b1a3b" stroke-width="1.5"><rect x="10" y="4" width="20" height="32"/><path d="M14 9h12M14 13h12"/><circle cx="20" cy="19" r="3"/><path d="M14 32v-4M18 32v-6M22 32v-3M26 32v-7"/></svg><p>STREAMLINED<br>EXPENSE REPORTS</p></div>
<div class="abs feature" style="left:705px"><svg width="40" height="40" viewBox="0 0 40 40" fill="none" stroke="#0b1a3b" stroke-width="1.5"><path d="M6 6h24l4 4v24H6z"/><path d="M12 6v9h14V6M22 8v5"/><rect x="11" y="21" width="18" height="13"/></svg><p>UNPARALLELED<br>SAVINGS</p></div>
<div class="abs feature" style="left:903px"><svg width="40" height="40" viewBox="0 0 40 40" fill="none" stroke="#0b1a3b" stroke-width="1.5"><circle cx="18" cy="14" r="6"/><circle cx="18" cy="14" r="2"/><circle cx="31" cy="8" r="3"/><circle cx="31" cy="20" r="3"/><path d="M4 28h7l6 2h7M4 34h8l8 1 14-7-2-2-8 3"/></svg><p>FULL SERVICE<br>TRAVEL MANAGEMENT</p></div>

<!-- footer -->
<footer class="abs site-footer"></footer>
<div class="abs foot-circle"></div>
<div class="abs foot-brand">MERIDIAN TRAVEL</div>
<div class="abs social" style="left:277px" aria-label="Social link"></div>
<div class="abs social on" style="left:313px" aria-label="Social link"></div>
<div class="abs social" style="left:349px" aria-label="Social link"></div>
<div class="abs social" style="left:385px" aria-label="Social link"></div>
<div class="abs vline" style="left:485px"></div>
<div class="abs vline" style="left:774px"></div>

<h4 class="abs foot-h" style="left:544px;top:3101px">CONTACT US</h4>
<div class="abs foot-u" style="left:544px;top:3133px;width:153px"></div>
<div class="abs foot-item" style="left:544px;top:3155px"><svg width="12" height="16" viewBox="0 0 12 16" fill="#fff"><path d="M6 0a6 6 0 0 0-6 6c0 4.5 6 10 6 10s6-5.5 6-10a6 6 0 0 0-6-6zm0 8.5A2.5 2.5 0 1 1 6 3.5a2.5 2.5 0 0 1 0 5z"/></svg><span>Location name will be here<br>near this building 12345</span></div>
<div class="abs foot-item" style="left:544px;top:3207px;font-weight:600;color:#fff"><svg width="14" height="14" viewBox="0 0 14 14" fill="#fff"><path d="M3 0l3 3-2 2c1 2 3 4 5 5l2-2 3 3-2 3C6 14 0 8 0 3z"/></svg><span>555-014-2290</span></div>
<div class="abs foot-item" style="left:544px;top:3250px"><svg width="14" height="11" viewBox="0 0 14 11" fill="none" stroke="#fff" stroke-width="1.3"><rect x=".7" y=".7" width="12.6" height="9.6"/><path d="M1 1l6 5 6-5"/></svg><span style="text-decoration:underline">info@meridiantravel.example</span></div>

<h4 class="abs foot-h" style="left:834px;top:3101px">QUICK LINKS</h4>
<div class="abs foot-u" style="left:834px;top:3133px;width:106px"></div>
<span class="abs foot-link" style="top:3153px">HOME</span>
<span class="abs foot-link" style="top:3178px">ABOUT US</span>
<span class="abs foot-link" style="top:3202px">WHY CHOOSE US</span>
<span class="abs foot-link" style="top:3227px">RESOURCES</span>
<span class="abs foot-link" style="top:3251px">CONTACT</span>

<div class="abs copy-line"></div>
<p class="abs copy">©2023 meridiantravel.example | All Rights Reserved.</p>

</body>
</html>
```